Travel Blogger Business Card for wanderquill.net

I need a two-sided business card for a travel blogging website. The card should be both professional and fun at the same time. This is for the website www.wanderquill.net

I don't necessarily think that the current logo on the website needs to be used on the business card but it can be. I am very flexible with ideas

Target Market(s)

Travel agencies that will be met at a conference.

Industry/Entity Type

Travel

Contact Information for Business Card

Company Name: Wander Quill.net
Name: Marcel Vennor
Voice: +1-(555)-555-0193
Address: Coral Reed Shore, Port Halden, Isle of Merrow
Email: ceo@wanderquill.net

Colors
0592cd
0355a3
3176b5
33a6d7
85cae6
85acd3

Requirements
Must have
• Website address and name should be bigger than address, phone number, and email.

```html
<!DOCTYPE html>
<html lang="en">
<head>
<meta charset="utf-8">
<title>Wander Quill – Business Card</title>
<link href="https://fonts.googleapis.com/css2?family=Montserrat:wght@400;500;700;800&display=swap" rel="stylesheet">
<style>
  :root {
    --page: #d9dcdf;
    --card: #050505;
    --brand: #33a6d7;
    --accent: #0592cd;
    --ink: #f2f2f2;
    --muted: #cfcfcf;
    --rule: #5a5a5a;
  }
  * { margin: 0; padding: 0; box-sizing: border-box; }
  html, body { width: 1200px; height: 900px; overflow: hidden; }
  body {
    background: var(--page);
    font-family: "Montserrat", Arial, sans-serif;
    position: relative;
  }
  .card {
    position: absolute;
    left: 260px;
    width: 680px;
    height: 388px;
    background: var(--card);
    box-shadow: 0 10px 28px rgba(0,0,0,.25);
    overflow: hidden;
  }
  .card--front { top: 46px; }
  .card--back { top: 464px; }

  .brand {
    position: absolute;
    display: flex;
    align-items: center;
    gap: 14px;
  }
  .brand__dot {
    width: 18px; height: 18px;
    border-radius: 50%;
    background: var(--brand);
    flex: none;
  }
  .brand__name {
    color: var(--brand);
    font-weight: 800;
    letter-spacing: .5px;
    white-space: nowrap;
  }
  .card--front .brand { left: 100px; top: 176px; }
  .card--front .brand__name { font-size: 52px; }

  .site {
    position: absolute;
    left: 0; right: 0;
    bottom: 58px;
    text-align: center;
    color: var(--ink);
    font-size: 19px;
    font-weight: 400;
    letter-spacing: .3px;
  }
  .site b { font-weight: 700; }

  .card--back .brand { left: 48px; top: 250px; }
  .card--back .brand__name { font-size: 28px; }
  .card--back .brand__dot { width: 12px; height: 12px; }

  .divider {
    position: absolute;
    left: 358px; top: 116px;
    width: 1px; height: 142px;
    background: var(--rule);
  }
  .contact {
    position: absolute;
    left: 378px; top: 108px;
    color: var(--ink);
  }
  .contact__name {
    color: var(--accent);
    font-weight: 700;
    font-size: 17px;
    letter-spacing: .6px;
    text-transform: uppercase;
    margin-bottom: 8px;
  }
  .contact__address {
    font-size: 14px;
    line-height: 1.3;
    color: var(--muted);
    margin-bottom: 10px;
    padding-left: 10px;
  }
  .contact__list { list-style: none; }
  .contact__item {
    display: flex;
    align-items: center;
    gap: 10px;
    font-size: 14px;
    line-height: 1;
    margin-bottom: 8px;
  }
  .contact__item--web { font-size: 16px; }
  .contact__item--web b { font-weight: 700; }
  .icon {
    width: 18px; height: 18px;
    border-radius: 50%;
    background: var(--accent);
    display: flex; align-items: center; justify-content: center;
    flex: none;
  }
  .icon svg { width: 11px; height: 11px; }
</style>
</head>
<body>

  <section class="card card--front" aria-label="Business card front">
    <div class="brand">
      <span class="brand__dot"></span>
      <span class="brand__name">WANDER QUILL</span>
    </div>
    <p class="site">www.<b>wanderquill</b>.net</p>
  </section>

  <section class="card card--back" aria-label="Business card back">
    <div class="brand">
      <span class="brand__dot"></span>
      <span class="brand__name">WANDER QUILL</span>
    </div>
    <div class="divider"></div>
    <div class="contact">
      <p class="contact__name">Marcel Vennor</p>
      <p class="contact__address">Coral Reed Shore<br>Port Halden, Isle of Merrow</p>
      <ul class="contact__list">
        <li class="contact__item">
          <span class="icon"><svg viewBox="0 0 12 12"><path d="M2.5 1.5l2 .2.7 2.2-1.2.9a6 6 0 0 0 3.2 3.2l.9-1.2 2.2.7.2 2c-4.5.5-8.5-3.5-8-8z" fill="#050505"/></svg></span>
          <span>+1-(555)-555-0193</span>
        </li>
        <li class="contact__item">
          <span class="icon"><svg viewBox="0 0 12 12"><rect x="1.5" y="3" width="9" height="6" fill="none" stroke="#050505" stroke-width="1.2"/><path d="M1.5 3L6 6.5 10.5 3" fill="none" stroke="#050505" stroke-width="1.2"/></svg></span>
          <span>ceo@wanderquill.net</span>
        </li>
        <li class="contact__item contact__item--web">
          <span class="icon"><svg viewBox="0 0 12 12"><circle cx="6" cy="6" r="4.3" fill="none" stroke="#050505" stroke-width="1.1"/><ellipse cx="6" cy="6" rx="1.8" ry="4.3" fill="none" stroke="#050505" stroke-width="1"/><path d="M1.7 6h8.6" stroke="#050505" stroke-width="1"/></svg></span>
          <span>www.<b>wanderquill</b>.net</span>
        </li>
      </ul>
    </div>
  </section>

</body>
</html>
```